TK Joinery

Cabinet maker. Kitchens. Wardrobes. Vanitys. Entertainment units

Target Market(s)

Modern contemporary.geometry. colours black, gray, charcoal and orange. Matt card gloss letters

Industry/Entity Type

Entertainment

Contact Information for Business Card

Mattias Velder 0418 295 437
mattias.velder@fernmail.test
ABN 471 9052 8316

Font styles to use
Decorative

Colors
000000

Requirements
Should not have
• Pictures

```html
<!DOCTYPE html>
<html lang="en">
<head>
<meta charset="utf-8">
<title>TK Joinery – Business Card</title>
<link rel="stylesheet" href="https://fonts.googleapis.com/css2?family=Cinzel:wght@400&display=swap">
<style>
  :root {
    --page: #ffffff;
    --black: #000000;
    --charcoal: #1f1f21;
    --charcoal-mid: #2c2c2f;
    --gray: #4a4a4e;
    --gray-light: #6e6e73;
    --orange: #f07a1a;
    --orange-deep: #c9530a;
    --orange-light: #f6a04a;
    --ink: #ffffff;
  }
  * { margin: 0; padding: 0; box-sizing: border-box; }
  html, body {
    width: 1054px; height: 1200px; overflow: hidden;
    background: var(--page);
    font-family: "Cinzel", "Times New Roman", serif;
    font-weight: 400;
    color: var(--ink);
  }
  .canvas { position: relative; width: 1054px; height: 1200px; }

  .card {
    position: absolute; left: 81px; width: 894px; height: 529px;
    border: 2px solid var(--black);
    box-shadow: 2px 3px 6px rgba(0,0,0,.35);
  }
  .card--front { top: 46px; }
  .card--back { top: 636px; }

  .card__frame {
    position: absolute; inset: 0;
    background:
      repeating-linear-gradient(45deg, transparent 0 22px, rgba(255,255,255,.035) 22px 44px),
      linear-gradient(135deg, var(--gray) 0%, var(--charcoal) 55%, var(--black) 100%);
  }

  .card__field {
    position: absolute; left: 72px; top: 55px; width: 747px; height: 417px;
    border: 3px solid var(--orange);
    background:
      repeating-linear-gradient(90deg, transparent 0 82px, rgba(255,255,255,.05) 82px 84px),
      linear-gradient(180deg, var(--charcoal-mid) 0%, var(--charcoal) 55%, var(--black) 100%);
  }

  .front__title {
    position: absolute; left: 0; right: 0; top: 140px;
    text-align: center; font-size: 84px; font-weight: 400; line-height: 1;
    letter-spacing: 1px;
  }
  .front__rule {
    position: absolute; left: 105px; width: 685px; height: 2px; background: var(--orange);
  }
  .front__rule--top { top: 276px; }
  .front__rule--bottom { top: 381px; }
  .front__services {
    position: absolute; left: 0; right: 0; top: 292px;
    text-align: center; font-size: 31px; line-height: 39px; letter-spacing: 1px;
  }
  .front__services span { margin: 0 8px; }

  .card__panel {
    position: absolute; left: 77px; top: 61px; width: 740px; height: 406px;
    background: linear-gradient(135deg, var(--orange-light) 0%, var(--orange) 45%, var(--orange-deep) 100%);
    border-left: 6px solid var(--black);
  }
  .back__name {
    position: absolute; left: 96px; top: 84px; font-size: 45px; font-weight: 400; line-height: 1; letter-spacing: 1px;
  }
  .back__rule {
    position: absolute; left: 96px; top: 146px; width: 335px; height: 2px; background: var(--charcoal);
  }
  .back__contact {
    position: absolute; left: 96px; font-size: 27px; line-height: 34px; letter-spacing: .5px;
  }
  .back__address { top: 160px; }
  .back__address .indent { padding-left: 34px; }
  .back__phones { top: 246px; }
  .back__phones .gap { display: inline-block; width: 26px; }
  .back__email { top: 300px; font-size: 25px; }
  .back__abn { top: 346px; font-size: 25px; }
  .back__brand {
    position: absolute; right: 96px; top: 404px; font-size: 40px; font-weight: 400; line-height: 1; letter-spacing: 1px;
  }
</style>
</head>
<body>
<main class="canvas">

  <section class="card card--front" aria-label="Card front">
    <div class="card__frame"></div>
    <div class="card__field"></div>
    <h1 class="front__title">TK Joinery</h1>
    <div class="front__rule front__rule--top"></div>
    <p class="front__services">
      <span>Cabinet maker</span><span>Kitchens</span><span>Wardrobes</span><br>
      <span>Vanitys</span><span>Entertainment units</span>
    </p>
    <div class="front__rule front__rule--bottom"></div>
  </section>

  <section class="card card--back" aria-label="Card back">
    <div class="card__frame"></div>
    <div class="card__panel"></div>
    <h2 class="back__name">Mattias Velder</h2>
    <div class="back__rule"></div>
    <p class="back__contact back__address">A: 58 Tallow Rd. Unit 12<br><span class="indent">Brookvale, NSW 2100</span></p>
    <p class="back__contact back__phones">P: 0418 295 437<span class="gap"></span>F: 0418 295 437</p>
    <p class="back__contact back__email">E: mattias.velder@fernmail.test</p>
    <p class="back__contact back__abn">ABN: 471 9052 8316</p>
    <p class="back__brand">TK Joinery</p>
  </section>

</main>
</body>
</html>
```